Very visible CoWorking Building Sign overlooking downtown LA and 110 freeway

Our building is drab but very visible and in the best location. We need a great sign for our monolith that overlooks downtown LA and the 100 freeway. We are a new CoWorking business and would like to have a few things we do on the sign: private offices, virtual offices, CoWorking Lounge. Everything we have seen is ho-hum. Can you get us noticed? We need people to know what we do and that we are here but in a creative, professional, unique sign.
Target Market(s)
People who have a business in DTLA, remote workers and those who work from home who need a professional address.
Requirements
Must have
- Our logo (which can be somewhat reimagined) which has our address 2770 on it. The three things we focus on: Private Offices, Virtual Offices, CoWorking Lounge. Incorporate some Navy. Readable from several hundred feet away.
Nice to have
- Mural feel? Something inspirational in this crazy COVID times? Graphics? Color block. I like the idea of decorative but it has to be readable as a building sign. The same with the use of colors. Our colors are grays and navy but with a pop of the chartreuse (we have 2 velvet chartreuse chairs in the space). Helpful to view our website: Brackmere2770.com.
Should not have
- Not too graffiti. Keep it professional but unique and wow.

```html
<!DOCTYPE html>
<html lang="en">
<head>
<meta charset="utf-8">
<title>Brackmere2770 Coworking Building Sign</title>
<link rel="stylesheet" href="https://fonts.googleapis.com/css2?family=Montserrat:wght@600;800&display=swap">
<style>
  :root {
    --backdrop: #5e5e5e;
    --navy: #023e7b;
    --ink-navy: #0b3770;
    --logo-navy: #1a335c;
    --green-dark: #76a812;
    --green-light: #9bc93c;
    --gold: #cdb500;
    --white: #ffffff;
    --mist-top: #ffffff;
    --mist-bottom: #f0f0f0;
  }
  html, body {
    margin: 0;
    padding: 0;
    width: 982px;
    height: 1200px;
    overflow: hidden;
    background: var(--backdrop);
  }
  .stage {
    position: relative;
    width: 982px;
    height: 1200px;
  }
  .building-sign {
    position: absolute;
    left: 0;
    top: 0;
    width: 982px;
    height: 1200px;
  }
  .sign-text {
    font-family: "Montserrat", Arial, sans-serif;
  }
  .brand-name {
    font-weight: 600;
    fill: var(--logo-navy);
  }
  .service-label {
    font-weight: 800;
    fill: var(--ink-navy);
    font-size: 82px;
  }
  .phone-number {
    font-weight: 800;
    fill: var(--white);
    font-size: 118px;
    letter-spacing: 6px;
  }
  .field-mist { fill: url(#mistGradient); }
  .band-navy { fill: var(--navy); }
  .wedge-dark { fill: var(--green-dark); }
  .wedge-light { fill: var(--green-light); }
  .pill { fill: var(--white); }
  .badge-ring { fill: var(--navy); }
  .badge { fill: var(--gold); }
  .arrow { fill: none; stroke: var(--white); stroke-width: 14; stroke-linecap: round; stroke-linejoin: round; }
  .phone-band { fill: var(--gold); }
  .phone-icon { fill: var(--white); }
  .phone-waves { fill: none; stroke: var(--white); stroke-width: 5; stroke-linecap: round; }
</style>
</head>
<body>
<main class="stage">
  <svg class="building-sign" viewBox="0 0 1736 2122" xmlns="http://www.w3.org/2000/svg" aria-label="Brackmere2770 coworking sign">
    <defs>
      <linearGradient id="mistGradient" x1="0" y1="0" x2="1" y2="1">
        <stop offset="0" stop-color="var(--mist-top)"/>
        <stop offset="1" stop-color="var(--mist-bottom)"/>
      </linearGradient>
    </defs>

    <!-- upper light field -->
    <rect class="field-mist" x="194" y="218" width="1348" height="920" role="img" aria-label="Soft grey field with faint dot and diamond texture"/>

    <!-- colour-block wedges -->
    <polygon class="wedge-dark" points="194,858 617,1128 194,963"/>
    <polygon class="wedge-light" points="500,1053 1193,828 1139,858 617,1128"/>
    <polygon class="wedge-dark" points="1193,828 1542,963 1542,1117 1139,858"/>
    <polygon class="band-navy" points="194,963 617,1128 1139,858 1542,1117 1542,1903 194,1903"/>

    <!-- brand name -->
    <g class="sign-text brand-name">
      <text x="300" y="500" font-size="110">2770</text>
      <text x="300" y="698" font-size="200" textLength="1130" lengthAdjust="spacingAndGlyphs">BRACKMERE</text>
      <text x="1156" y="797" font-size="92" textLength="276" lengthAdjust="spacingAndGlyphs">.COM</text>
    </g>

    <!-- services -->
    <g class="service">
      <rect class="pill" x="400" y="1168" width="1026" height="125" rx="62.5"/>
      <circle class="badge-ring" cx="379" cy="1230" r="73"/>
      <circle class="badge" cx="373" cy="1230" r="72"/>
      <path class="arrow" d="M342 1230 H402 M376 1206 L402 1230 L376 1254"/>
      <text class="sign-text service-label" x="484" y="1259" textLength="694" lengthAdjust="spacingAndGlyphs">PRIVATE OFFICES</text>
    </g>
    <g class="service">
      <rect class="pill" x="400" y="1349" width="1026" height="125" rx="62.5"/>
      <circle class="badge-ring" cx="379" cy="1411" r="73"/>
      <circle class="badge" cx="373" cy="1411" r="72"/>
      <path class="arrow" d="M342 1411 H402 M376 1387 L402 1411 L376 1435"/>
      <text class="sign-text service-label" x="490" y="1440" textLength="708" lengthAdjust="spacingAndGlyphs">VIRTUAL OFFICES</text>
    </g>
    <g class="service">
      <rect class="pill" x="400" y="1530" width="1026" height="125" rx="62.5"/>
      <circle class="badge-ring" cx="379" cy="1592" r="73"/>
      <circle class="badge" cx="373" cy="1592" r="72"/>
      <path class="arrow" d="M342 1592 H402 M376 1568 L402 1592 L376 1616"/>
      <text class="sign-text service-label" x="486" y="1621" textLength="856" lengthAdjust="spacingAndGlyphs">COWORKING LOUNGE</text>
    </g>

    <!-- phone band -->
    <rect class="phone-band" x="194" y="1722" width="1348" height="135"/>
    <g class="phone">
      <path class="phone-icon" d="M352 1746 C340 1756 340 1782 356 1806 C372 1830 396 1842 414 1838 C424 1836 432 1830 434 1824 L412 1800 C406 1806 398 1810 392 1806 C382 1798 372 1784 368 1772 C366 1766 370 1760 376 1756 L362 1744 Z"/>
      <path class="phone-waves" d="M398 1770 A12 12 0 0 1 410 1782 M398 1756 A26 26 0 0 1 424 1782 M398 1742 A40 40 0 0 1 438 1782"/>
      <text class="sign-text phone-number" x="488" y="1832" textLength="912" lengthAdjust="spacingAndGlyphs">+310-555-2770</text>
    </g>
  </svg>
</main>
</body>
</html>
```